Nonprofit K-8 Korbane School. Elementary education ( please google Korbane Schools)

We are a nonprofit Korbane School in the U.S.
We need to advertise our school using yard signs. The information should be easy to see from a distance. Clear and concise, using large print without additional design outside of the logo itself. It should have our logo as the header, with the following text centered below the logo:
Open House!
Feb 10th, March 10th and April 21st.
Call 555 014-2967 for more information

Target Market(s)

Parents of children between ages of 5 yrs to 13yrs old

Industry/Entity Type

School

Other font styles liked:
• Formal436bt

Colors
ec1f27
ffffff

Requirements
Must have
• It must have our uploaded logo as the header, and the following information below using the font Formal436bt:
• Open House!
• Feb 10th, March 10th and April 21st.
• Call 555 014-2967 for more information
Should not have
• Any other color but the red and white indicated on our logo

```html
<!DOCTYPE html>
<html lang="en">
<head>
<meta charset="utf-8">
<title>Elmsway School – Open House Yard Sign</title>
<link rel="stylesheet" href="https://fonts.googleapis.com/css2?family=Marcellus&family=Roboto+Condensed:wght@700&display=swap">
<style>
  :root {
    --red: #ec1f27;
    --red-deep: #c4151c;
    --white: #ffffff;
    --backdrop: #e9e9e9;
  }
  html, body {
    margin: 0;
    padding: 0;
    width: 746px;
    height: 1200px;
    overflow: hidden;
    background: var(--backdrop);
  }
  .canvas {
    width: 746px;
    height: 1200px;
    display: flex;
    align-items: center;
    justify-content: center;
  }
  .yard-sign {
    width: 634px;
    height: 446px;
    display: block;
    box-shadow: 0 6px 18px rgba(0,0,0,0.18);
  }
  .school-name { font-family: "Marcellus", serif; fill: var(--white); font-size: 30px; }
  .headline { font-family: "Marcellus", serif; fill: var(--red); font-size: 72px; }
  .dates { font-family: "Roboto Condensed", sans-serif; font-weight: 700; fill: var(--white); font-size: 29px; }
  .info-label { font-family: "Roboto Condensed", sans-serif; font-weight: 700; fill: var(--white); font-size: 16px; }
  .phone { font-family: "Roboto Condensed", sans-serif; font-weight: 700; fill: var(--white); font-size: 34px; }
</style>
</head>
<body>
<main class="canvas">
  <svg class="yard-sign" viewBox="0 0 634 446" xmlns="http://www.w3.org/2000/svg" aria-label="Elmsway School open house yard sign">
    <defs>
      <linearGradient id="header-red" x1="0" y1="0" x2="0" y2="1">
        <stop offset="0" stop-color="#d8141c"/>
        <stop offset="0.45" stop-color="#ec1f27"/>
        <stop offset="1" stop-color="#c4151c"/>
      </linearGradient>
      <linearGradient id="house-fade" x1="0" y1="0" x2="0" y2="1">
        <stop offset="0" stop-color="#c4151c"/>
        <stop offset="1" stop-color="#ffffff"/>
      </linearGradient>
    </defs>

    <rect class="sign-field" x="0" y="0" width="634" height="446" fill="var(--white)"/>
    <rect class="header-field" x="0" y="0" width="634" height="160" fill="url(#header-red)"/>
    <rect class="house-illustration" x="0" y="160" width="634" height="80" fill="url(#house-fade)"
          role="img" aria-label="House roof and chimney illustration framing the headline"/>

    <rect class="logo-square" x="150" y="72" width="32" height="32" fill="var(--white)"/>
    <text class="school-name" x="196" y="101" textLength="301" lengthAdjust="spacingAndGlyphs">ELMSWAY SCHOOL</text>

    <text class="headline" x="349" y="318" text-anchor="middle" textLength="485" lengthAdjust="spacingAndGlyphs">OPEN HOUSE</text>

    <rect class="details-band" x="71" y="355" width="563" height="91" fill="var(--red)"/>
    <text class="dates" x="94" y="390" textLength="495" lengthAdjust="spacingAndGlyphs">FEB 10TH, MAR 10TH AND APRIL 21ST</text>
    <text class="info-label" x="94" y="421" textLength="200" lengthAdjust="spacingAndGlyphs">FOR MORE INFORMATION</text>
    <text class="phone" x="302" y="430" textLength="289" lengthAdjust="spacingAndGlyphs">CALL: 555 014-2967</text>
  </svg>
</main>
</body>
</html>
```